Small Cosmetics Business needs a label design

We need a label design to affix on our cosmetic products made in Norfolk, England. The label needs to have the manufacturer's name, the product name, an ingredients list, an indication of use (ritual), contact details of manufacturer, weight, period after opening logo, batch number. We would like the label to highlight (in the form of sticker or tags) that the products are 100% natural, that they are hand made, that they do not contain preservatives or chemicals.Attached is a file with typical information for the label. The label should have colours, clarity and evoke nature, luxury.

Target Market(s)

UK

Industry/Entity Type

Cosmetics

Logo Text

Tobri Seku, Find Radiance

Font styles to use
Decorative

```html
<!DOCTYPE html>
<html lang="en">
<head>
<meta charset="utf-8">
<title>Tobri Seku – Coco Bloom label</title>
<link href="https://fonts.googleapis.com/css2?family=Open+Sans:ital,wght@0,400;0,600;0,700;1,400;1,700&family=Kaushan+Script&display=swap" rel="stylesheet">
<style>
  :root{
    --leaf-green:#3cb44a;
    --lime:#b6d45a;
    --olive:#9aaa3a;
    --olive-dark:#6f7d22;
    --sun:#f6b61b;
    --lemon:#f1ee3a;
    --ink:#111111;
    --paper:#ffffff;
    --rule:#222222;
  }
  *{box-sizing:border-box;margin:0;padding:0}
  html,body{width:1200px;height:622px;overflow:hidden;background:var(--paper)}
  body{position:relative;font-family:"Open Sans",Arial,sans-serif;color:var(--ink)}

  .brand-head{position:absolute;left:0;top:100px;width:1200px;display:flex;justify-content:center;align-items:center;gap:14px}
  .brand-head__dot{width:16px;height:16px;border-radius:50%;background:var(--sun)}
  .brand-head__name{font-weight:600;font-size:50px;line-height:1;color:var(--leaf-green);letter-spacing:1px}

  .label{position:absolute;left:31px;top:263px;width:1152px;height:211px;border:1px solid var(--rule);display:flex;background:var(--paper)}
  .panel{position:relative;height:100%;overflow:hidden}
  .panel--info{width:373px;border-right:1px solid var(--rule);
    background:
      linear-gradient(135deg,rgba(241,238,58,.75) 0%,rgba(241,238,58,.25) 22%,rgba(255,255,255,0) 40%),
      linear-gradient(215deg,rgba(241,238,58,.55) 0%,rgba(255,255,255,0) 28%),
      var(--paper)}
  .panel--front{width:380px;border-right:1px solid var(--rule)}
  .panel--ingredients{flex:1;
    background:
      linear-gradient(225deg,rgba(241,238,58,.8) 0%,rgba(241,238,58,.3) 20%,rgba(255,255,255,0) 38%),
      linear-gradient(320deg,rgba(241,238,58,.6) 0%,rgba(255,255,255,0) 30%),
      var(--paper)}

  .heading{font-weight:600;font-size:13px;line-height:16px}
  .body-text{font-size:10.5px;line-height:15px}

  .ritual{position:absolute;left:13px;top:12px;width:345px}
  .ritual .heading{margin-bottom:3px}
  .maker{position:absolute;left:13px;top:92px}
  .maker .heading{margin-bottom:4px}
  .batch{position:absolute;left:13px;top:147px}
  .weight{position:absolute;left:13px;top:181px}
  .panel-mark{position:absolute;left:255px;top:177px;font-weight:600;font-size:13px;line-height:16px;color:var(--leaf-green)}

  .front-mark{position:absolute;left:0;top:32px;width:100%;text-align:center;font-weight:600;font-size:13px;line-height:16px;color:var(--leaf-green)}
  .product-ribbon{position:absolute;left:0;top:0}
  .product-name{position:absolute;left:103px;top:66px;width:200px;height:36px;display:flex;align-items:center;justify-content:center;font-family:"Kaushan Script",cursive;font-size:26px;line-height:1;color:var(--ink)}
  .product-tagline{position:absolute;left:209px;top:103px;font-style:italic;font-size:11px;line-height:14px}
  .natural-pct{position:absolute;left:20px;top:161px;width:40px;text-align:center;font-weight:600;font-size:13px;line-height:16px}
  .natural-text{position:absolute;left:73px;top:160px;font-style:italic;font-size:14px;line-height:18px}
  .claims{position:absolute;left:194px;top:158px;list-style:none}
  .claims li{position:relative;padding-left:13px;font-style:italic;font-size:11px;line-height:10px;margin-bottom:8px}
  .claims li::before{content:"»";position:absolute;left:0;top:-2px;font-style:normal;font-weight:700;font-size:13px;color:var(--sun)}

  .ingredients{position:absolute;left:16px;top:12px;width:350px}
  .ingredients .heading{margin-bottom:3px}
  .ingredients .body-text{line-height:15.4px}
  .pao{position:absolute;left:158px;top:144px}
  .pao-note{position:absolute;left:118px;top:188px;font-size:8px;line-height:10px}
</style>
</head>
<body>
  <header class="brand-head">
    <span class="brand-head__dot"></span>
    <span class="brand-head__name">Tobri Seku</span>
  </header>

  <section class="label">
    <div class="panel panel--info">
      <div class="ritual">
        <h3 class="heading">Ritual:</h3>
        <p class="body-text">Use for wet or dry hair. Apply to the length of the hair focussing on the ends. Leave <strong><em>15 minutes</em></strong> then rinse with either water or a light shampoo and style as wished.</p>
      </div>
      <div class="maker">
        <h3 class="heading">Manufactured by</h3>
        <p class="body-text">Tobri Seku Ltd, P.O. Box 418 Holtmere HM7 2QS, UK</p>
      </div>
      <h3 class="heading batch">Batch number:</h3>
      <h3 class="heading weight">Weight:</h3>
      <span class="panel-mark">Tobri Seku</span>
    </div>

    <div class="panel panel--front">
      <span class="front-mark">Tobri Seku</span>
      <svg class="product-ribbon" width="380" height="211" viewBox="0 0 380 211" aria-hidden="true">
        <polygon points="47,83 128,83 128,121 47,121 60,102" fill="var(--olive)"/>
        <polygon points="103,66 319,66 304,84 319,102 103,102" fill="var(--lime)"/>
        <polygon points="103,102 128,102 128,121" fill="var(--olive-dark)"/>
        <polygon points="61,158 147,158 139,170 147,182 61,182" fill="var(--lime)"/>
        <circle cx="40" cy="169" r="28" fill="var(--sun)"/>
        <circle cx="40" cy="169" r="22" fill="var(--paper)"/>
      </svg>
      <div class="product-name">Coco Bloom</div>
      <div class="product-tagline">for beautiful hair</div>
      <span class="natural-pct">100%</span>
      <span class="natural-text">Natural</span>
      <ul class="claims">
        <li>Handmade in Norfolk</li>
        <li>Contains No Preservatives<br>and No Chemicals</li>
      </ul>
    </div>

    <div class="panel panel--ingredients">
      <div class="ingredients">
        <h3 class="heading">Ingredients:</h3>
        <p class="body-text">Cocos NuciferaCoconut) Oil , ElaeisGuineensis (Sustainable Palm) Oil, Olea Europaea (Olive) Fruit Oil, Helianthus Annus (Sunflower) Seed Oil, ButyrospermumParkii (Shea Butter), OryzaSativa (Rice Bran) Oil,ArganiaSpinosa Kernel (Argan) Oil, PerseaGratissima (Avocado) Oil,SimmondsiaChinensis (Jojoba) Seed Oil, RicinusCommunis (Castor) Seed Oil, Cera Alba (Beeswax), CanagaOdorata (YlangYlang) Flower Oil, Citrus Aurantium Dulcis (Orange) Peel Oil.</p>
      </div>
      <svg class="pao" width="40" height="42" viewBox="0 0 40 42" role="img" aria-label="Period after opening: 3 months">
        <path d="M5 18 L33 2 L36 5 L7 20 Z" fill="none" stroke="var(--ink)" stroke-width="1"/>
        <path d="M3 23 L37 23 L35 40 L5 40 Z" fill="var(--paper)" stroke="var(--ink)" stroke-width="1.1"/>
        <text x="20" y="36" text-anchor="middle" font-family="Open Sans, Arial, sans-serif" font-size="10" fill="var(--ink)">3M</text>
      </svg>
      <p class="pao-note">Use within 3 Months after opening</p>
    </div>
  </section>
</body>
</html>
```